Business Card for Start Up Real Estate Company

We need a business card designed for a new real estate company called Lumivane. We plan on improving the experience of real estate transactions for both consumers and agents by using current and evolving technology. We would like to see designs that use our existing logo (attached). Please use a primarily white or light colored background. The final design should communicate technology, sophistication and customer service. Thank you...

Industry/Entity Type

Real Estate

Requirements
Must have
• Primarily white or light colored background
Nice to have
• Isolated A from our logo used as part of the design
Should not have
• Pictures, especially of houses

```html
<!DOCTYPE html>
<html lang="en">
<head>
<meta charset="utf-8">
<title>Lumivane Business Card</title>
<link rel="stylesheet" href="https://fonts.googleapis.com/css2?family=Arimo:wght@400;500&display=swap">
<style>
  :root {
    --brand-blue: #1c5a97;
    --brand-red: #e3263f;
    --rule-grey: #9a9a9a;
    --ink: #2e2e2e;
    --card-white: #ffffff;
    --backdrop: #ebe7e0;
    --card-edge: #3a3a3a;
    --mark-tint-a: #e4ebf4;
    --mark-tint-b: #f6e4e7;
  }
  * { box-sizing: border-box; margin: 0; padding: 0; }
  html, body {
    width: 1200px;
    height: 884px;
    overflow: hidden;
    background: var(--backdrop);
    font-family: "Arimo", Arial, sans-serif;
  }
  .business-card {
    position: absolute;
    left: 100px;
    top: 134px;
    width: 1000px;
    height: 616px;
    background: var(--card-white);
    border: 2px solid var(--card-edge);
    overflow: hidden;
  }
  .accent-top {
    position: absolute;
    top: 0;
    left: 599px;
    right: 0;
    height: 12px;
    background: var(--brand-red);
  }
  .accent-bottom-blue {
    position: absolute;
    bottom: 6px;
    left: 0;
    width: 599px;
    height: 14px;
    background: var(--brand-blue);
  }
  .accent-bottom-red {
    position: absolute;
    bottom: 8px;
    left: 599px;
    right: 0;
    height: 4px;
    background: var(--brand-red);
  }
  .wordmark {
    position: absolute;
    left: 37px;
    top: 88px;
    font-size: 98px;
    font-weight: 400;
    letter-spacing: 2px;
    color: var(--brand-blue);
    line-height: 1;
    text-transform: uppercase;
  }
  .divider {
    position: absolute;
    left: 37px;
    top: 266px;
    width: 555px;
    height: 3px;
    background: var(--rule-grey);
  }
  .holder-name {
    position: absolute;
    left: 673px;
    top: 252px;
    font-size: 40px;
    color: var(--brand-red);
    line-height: 1;
  }
  .address {
    position: absolute;
    left: 37px;
    top: 322px;
    font-size: 28px;
    line-height: 52px;
    color: var(--ink);
    font-style: normal;
  }
  .contact-row {
    position: absolute;
    left: 37px;
    display: flex;
    align-items: center;
    gap: 18px;
    font-size: 28px;
    color: var(--ink);
  }
  .contact-phone { top: 430px; }
  .contact-email { top: 496px; }
  .contact-icon { width: 46px; height: 46px; flex: none; }
  .monogram-watermark {
    position: absolute;
    left: 760px;
    top: 345px;
    width: 220px;
    height: 220px;
    border-radius: 50%;
    background: linear-gradient(160deg, var(--mark-tint-a) 0%, var(--mark-tint-a) 55%, var(--mark-tint-b) 100%);
    opacity: 0.8;
  }
</style>
</head>
<body>
  <main class="business-card">
    <div class="accent-top"></div>

    <div class="wordmark">Lumivane</div>
    <div class="divider"></div>

    <div class="holder-name">Dana R. Whitfield</div>

    <address class="address">
      4530 Brookline Avenue<br>
      Fairview, TN 38112
    </address>

    <div class="contact-row contact-phone">
      <svg class="contact-icon" viewBox="0 0 46 46" aria-hidden="true">
        <circle cx="23" cy="23" r="20" fill="none" stroke="#2e2e2e" stroke-width="2"/>
        <path d="M17 12c-2 1-3 3-3 6 0 7 6 15 12 17 2 1 4 0 6-2l-4-5-3 2c-3-2-5-6-5-9l3-2-2-6z" fill="none" stroke="#2e2e2e" stroke-width="2" stroke-linejoin="round"/>
      </svg>
      <span>901-555-0147</span>
    </div>

    <div class="contact-row contact-email">
      <svg class="contact-icon" viewBox="0 0 46 46" aria-hidden="true">
        <rect x="4" y="10" width="38" height="26" fill="none" stroke="#2e2e2e" stroke-width="2"/>
        <path d="M4 10l19 15 19-15" fill="none" stroke="#2e2e2e" stroke-width="2"/>
      </svg>
      <span>danawhitfield@lumivane.com</span>
    </div>

    <div class="monogram-watermark" role="img" aria-label="Faint brand monogram watermark"></div>

    <div class="accent-bottom-blue"></div>
    <div class="accent-bottom-red"></div>
  </main>
</body>
</html>
```